quarry productions business cards design

design a clean look but creative business card for a production company, I'm a freelance producer and launching my startup, would like to keep a clean professional look but still creative

Target Market(s)

businesses

Industry/Entity Type

video production

Contact Information for Business Card

logo, name (Karl Benn), Title (Producer), (MFA Filmmaking, QTSA Los Angeles), contact number & email ID

Colors

Designer to choose only greyscale colors for use in the design.

Requirements
Must have
• logo, black and white colors, you can play with their shades
Nice to have
• a unique design, not necessarily a typical size card
Should not have
• too colorful or playful

```html
<!DOCTYPE html>
<html lang="en">
<head>
<meta charset="utf-8">
<title>Quarry Productions — Business Cards</title>
<link href="https://fonts.googleapis.com/css2?family=Montserrat:wght@400;700&display=swap" rel="stylesheet">
<style>
  :root {
    --backdrop: #2b2b2d;
    --card: #1f1d1e;
    --card-deep: #181617;
    --pattern-a: #242223;
    --pattern-b: #2f2d2e;
    --silver: #d6d6d6;
    --text-main: #f2f2f2;
    --text-soft: #bdbdbd;
    --rule: #6a6a6a;
  }
  * { margin: 0; padding: 0; box-sizing: border-box; }
  html, body {
    width: 1200px; height: 800px; overflow: hidden;
    background: var(--backdrop);
    font-family: "Montserrat", Arial, sans-serif;
  }
  .canvas { position: relative; width: 1200px; height: 800px; }
  .card {
    position: absolute; width: 600px; height: 343px;
    border-radius: 22px; overflow: hidden;
    background: var(--card);
    box-shadow: 0 18px 40px rgba(0,0,0,.45);
  }
  .card-back { left: 150px; top: 50px; background: var(--card-deep); }
  .back-texture {
    position: absolute; inset: 0;
    background: linear-gradient(135deg, var(--pattern-b), var(--pattern-a) 60%, var(--card-deep));
  }
  .back-brand {
    position: absolute; left: 50%; bottom: 58px; transform: translateX(-50%);
    display: flex; align-items: center; gap: 8px;
    color: var(--silver); font-weight: 700; font-size: 15px; letter-spacing: .04em;
    white-space: nowrap;
  }
  .card-front { left: 450px; top: 410px; }
  .front-brand {
    position: absolute; left: 40px; top: 0; bottom: 0; width: 270px;
    display: flex; align-items: center; justify-content: center; gap: 12px;
    color: var(--silver); font-weight: 700; font-size: 24px; letter-spacing: .02em;
    white-space: nowrap;
  }
  .brand-dot { width: 12px; height: 12px; border-radius: 50%; background: var(--silver); flex: none; }
  .divider {
    position: absolute; left: 332px; top: 38px; bottom: 38px;
    width: 1px; background: var(--rule);
  }
  .details { position: absolute; left: 358px; top: 46px; right: 20px; }
  .name { color: var(--text-main); font-weight: 700; font-size: 21px; letter-spacing: .02em; }
  .credentials { margin-top: 4px; color: var(--text-soft); font-size: 13px; line-height: 1.4; }
  .contacts { list-style: none; margin-top: 38px; }
  .contacts li {
    display: flex; align-items: center; gap: 9px;
    color: var(--text-soft); font-size: 12px; line-height: 1; margin-bottom: 10px;
    white-space: nowrap;
  }
  .contacts svg { width: 13px; height: 13px; flex: none; }
</style>
</head>
<body>
<main class="canvas">
  <section class="card card-back" aria-label="Card back">
    <div class="back-texture" role="img" aria-label="Faint repeating brand pattern in dark greys"></div>
    <div class="back-brand"><span class="brand-dot"></span>quarry productions</div>
  </section>

  <section class="card card-front" aria-label="Card front">
    <div class="front-brand"><span class="brand-dot"></span>quarry productions</div>
    <div class="divider"></div>
    <div class="details">
      <h1 class="name">KARL BENN</h1>
      <p class="credentials">Producer<br>MFA in Filmmaking<br>QTSA, Los Angeles</p>
      <ul class="contacts">
        <li>
          <svg viewBox="0 0 16 16" aria-hidden="true"><path fill="#bdbdbd" d="M3.6 1.5l2.2 2.6-1.3 1.6c.9 2 2.4 3.5 4.3 4.4l1.6-1.3 2.6 2.2-1.4 2.2C7 13 3 9 1.8 4.3z"/></svg>
          200.555.0142
        </li>
        <li>
          <svg viewBox="0 0 16 16" aria-hidden="true"><rect x="1.5" y="3.5" width="13" height="9" fill="none" stroke="#bdbdbd" stroke-width="1.4"/><path d="M1.5 3.5L8 9l6.5-5.5" fill="none" stroke="#bdbdbd" stroke-width="1.4"/></svg>
          karlbenn@quarryproductions.com
        </li>
        <li>
          <svg viewBox="0 0 16 16" aria-hidden="true"><circle cx="8" cy="8" r="6.3" fill="none" stroke="#bdbdbd" stroke-width="1.3"/><ellipse cx="8" cy="8" rx="2.7" ry="6.3" fill="none" stroke="#bdbdbd" stroke-width="1.1"/><path d="M1.7 8h12.6" stroke="#bdbdbd" stroke-width="1.1"/></svg>
          www.quarryproductions.com
        </li>
      </ul>
    </div>
  </section>
</main>
</body>
</html>
```